Größen anpassen für versch. Werbemittel
Zielgruppe
Wir organisieren Messen rund um die Frau!
Aufgabenstellung
Das Layout steht soweit und müsste nur angepasst werden.
Wir benötigen folgendes:
Das beigefügte Plakat in folgenden Größen:
a1 - sollen bei Papierfalke gedruclt werden!
a3 - II
2m² Traffic Bord 120x75 ohne Beschnitt-Hochformat-Schriften vektorisieren!
Berliner Rahmen: Plakatdruck 2/1-(A0)-Querformat 84,1 x 118,5 cm, 115 g Affichenpapier 4-farbirg Euroskala
Großflächen: S. Anlage
LED Tafeln:
Immer der Fotocredit Brigitte Solweck dazu! Wichtig!
Das Logo aber sollte oben hin, dann das Foto, darunter der Text.
Irgendwo sollte noch dazu:
Die Trend- und Eventmesse rund um die Frau (oder ähnlich),
damit man direkt weiß, um was es geht ;)

```html
<!DOCTYPE html>
<html lang="de">
<head>
<meta charset="utf-8">
<title>VELORA – Trend- &amp; Eventmesse rund um die Frau</title>
<link rel="stylesheet" href="https://fonts.googleapis.com/css2?family=Open+Sans:wght@300;400;700&family=Kalam:wght@700&display=swap">
<style>
  :root {
    --berry: #c8186a;
    --ink: #1f1f1f;
    --slate: #555555;
    --paper: #ffffff;
    --rule: #9a9a9a;
    --photo-light: #ecebe8;
    --photo-warm: #c9a283;
    --photo-deep: #7a5a43;
  }
  html, body {
    margin: 0;
    padding: 0;
    overflow: hidden;
    background: var(--paper);
  }
  .poster {
    position: relative;
    width: 750px;
    height: 1200px;
    background: var(--paper);
    overflow: hidden;
    font-family: "Open Sans", Arial, sans-serif;
  }
  .brand {
    position: absolute;
    top: 42px;
    left: 0;
    width: 750px;
    text-align: center;
    font-family: "Open Sans", Arial, sans-serif;
    font-weight: 300;
    font-size: 118px;
    line-height: 1;
    letter-spacing: 22px;
    padding-left: 22px;
    box-sizing: border-box;
    color: var(--ink);
  }
  .hero-photo {
    position: absolute;
    top: 257px;
    left: 0;
    width: 750px;
    height: 535px;
    background:
      radial-gradient(ellipse 34% 46% at 52% 48%, var(--photo-warm) 0%, rgba(201,162,131,0.55) 55%, rgba(201,162,131,0) 100%),
      radial-gradient(ellipse 40% 30% at 22% 40%, rgba(122,90,67,0.35) 0%, rgba(122,90,67,0) 100%),
      linear-gradient(90deg, #d9d7d3 0%, var(--photo-light) 55%, #f4f3f1 100%);
  }
  .photo-credit {
    position: absolute;
    top: 761px;
    left: 59px;
    font-size: 11px;
    color: var(--ink);
  }
  .theme-band {
    position: absolute;
    top: 792px;
    left: 0;
    width: 750px;
    height: 135px;
    background: var(--berry);
    color: var(--paper);
    font-family: "Kalam", "Comic Sans MS", cursive;
    font-weight: 700;
    font-size: 41px;
    line-height: 48px;
    text-align: center;
    padding-top: 21px;
    box-sizing: border-box;
  }
  .event-date {
    position: absolute;
    top: 978px;
    left: 0;
    width: 750px;
    text-align: center;
    font-weight: 700;
    font-size: 27px;
    color: var(--slate);
  }
  .claim {
    position: absolute;
    top: 1035px;
    left: 0;
    width: 750px;
    text-align: center;
    font-weight: 400;
    font-size: 21px;
    line-height: 26px;
    color: var(--berry);
  }
  .divider {
    position: absolute;
    top: 1113px;
    left: 100px;
    width: 550px;
    height: 1px;
    background: var(--rule);
  }
  .web-address {
    position: absolute;
    top: 1121px;
    left: 0;
    width: 750px;
    text-align: center;
    font-weight: 700;
    font-size: 28px;
    color: var(--berry);
  }
</style>
</head>
<body>
  <main class="poster">
    <header class="brand">VELORA</header>

    <div class="hero-photo" role="img" aria-label="Porträtfoto einer lächelnden Frau mit schulterlangem braunem Haar vor hellem, unscharfem Hintergrund"></div>
    <p class="photo-credit" style="margin:0">Fotocredit: Brigitte Solweck</p>

    <section class="theme-band">
      TREND – &amp; EVENTMESSE<br>rund um die Frau
    </section>

    <p class="event-date" style="margin:0">29 &amp; 30 April 2017 - Tagungshaus Lindenhof</p>
    <p class="claim" style="margin:0">DEIN TAG ZUM WOHLFÜHLEN, SCHÖNSEIN,<br>LAUTLACHEN, SACHENMACHEN</p>

    <div class="divider"></div>
    <p class="web-address" style="margin:0">www.velora-events.de</p>
  </main>
</body>
</html>
```